Anzeigengestaltung für Fliesenlegermeister
Zielgruppe
Ich bin ein Fliesenlegermeister und möchte mich selbstständig machen, ich saniere Bäder, Böden mit Fliesen, Fliesenspiegel und ich möchte eine Anzeige in den regionalen Zeitungen machen. Ich spreche alle Altersklassen mit Bädern für Sanierungen, Bodenfliesen und Neubauten an. Reparatur und Silikonarbeiten sowie Trockenbauarbeiten am eigenen Heim .
Aufgabenstellung
Ich möchte gern meine Kontaktdaten und die Farben vom Logo wieder finden,
als Beispiel habe ich meine aktuelle Visitenkarte beigefügt Dort finden sich die Kontaktdaten. Meine Arbeiten sind insbesondere :
Fliesenverlegung
Badsanierung
barrierefreie Bäder
Reparaturarbeiten
Silikonarbeiten
Trockenbau
Ob nun genau alle 6 Punkte in der Anzeige angezeigt werden soll bin ich mir nicht sicher oder ob nur 4 Beschreibungen reichen, damit es nicht zu viel wird.

```html
<!DOCTYPE html>
<html lang="de">
<head>
<meta charset="utf-8">
<title>Anzeige Fliesenlegermeister Jonas Veltmann</title>
<link rel="stylesheet" href="https://fonts.googleapis.com/css2?family=Open+Sans:wght@400;600;700&display=swap">
<style>
  :root {
    --brand-blue: #0e4e9e;
    --slate: #47484b;
    --paper: #ffffff;
    --backdrop: #e4e5e7;
    --ink: #1c1c1e;
  }
  * { box-sizing: border-box; margin: 0; padding: 0; }
  html, body {
    width: 1200px; height: 803px; overflow: hidden;
    background: var(--backdrop);
    font-family: "Open Sans", Arial, sans-serif;
  }
  .advert {
    position: absolute; left: 365px; top: 31px;
    width: 470px; height: 740px;
    background: var(--paper);
    box-shadow: 0 2px 10px rgba(0,0,0,.12);
    overflow: hidden;
  }
  .brand {
    display: flex; align-items: center; gap: 16px;
    padding: 34px 0 0 36px;
  }
  .brand-square {
    width: 52px; height: 52px; background: var(--brand-blue);
    flex: none;
  }
  .brand-name {
    color: var(--brand-blue); font-weight: 700;
    font-size: 33px; line-height: 1; letter-spacing: .5px;
    border-left: 2px solid var(--ink); padding-left: 14px;
  }
  .brand-name small {
    display: block; font-size: 15.5px; letter-spacing: 2.6px; margin-top: 6px;
  }
  .services-title {
    margin: 48px 0 0 46px;
    color: var(--brand-blue); font-weight: 700; font-size: 25px;
  }
  .services {
    list-style: none; margin: 10px 0 0 46px;
  }
  .services li {
    display: flex; align-items: center; gap: 14px;
    font-size: 27px; color: var(--ink); line-height: 1.45;
  }
  .services li::before {
    content: ""; width: 14px; height: 14px; flex: none;
    background: var(--brand-blue); transform: rotate(45deg);
  }
  .owner-band {
    position: absolute; left: 0; top: 466px;
    width: 100%; height: 86px;
    background: var(--brand-blue); color: var(--paper);
    padding: 16px 0 0 30px;
  }
  .owner-name { font-size: 25px; font-weight: 700; }
  .owner-title { font-size: 15px; }
  .contact-panel {
    position: absolute; left: 0; top: 552px;
    width: 100%; height: 188px;
    background: var(--slate); color: var(--paper);
    padding: 20px 0 0 30px;
  }
  .contact-list { list-style: none; }
  .contact-list li {
    display: flex; align-items: flex-start; gap: 11px;
    font-size: 14.5px; line-height: 1.35; margin-bottom: 10px;
  }
  .contact-icon {
    width: 24px; height: 19px; background: var(--paper);
    flex: none; display: flex; align-items: center; justify-content: center;
    margin-top: 0;
  }
  .contact-icon svg { width: 13px; height: 13px; }
  .tile-accent {
    position: absolute; right: 0; top: 466px; width: 110px; height: 274px;
  }
</style>
</head>
<body>
  <section class="advert">
    <header class="brand">
      <span class="brand-square"></span>
      <div class="brand-name">JONAS VELTMANN<small>FLIESENLEGERMEISTER</small></div>
    </header>

    <h2 class="services-title">Unsere Leistungen :</h2>
    <ul class="services">
      <li>Fliesenverlegung</li>
      <li>Badsanierung</li>
      <li>barrierefreie Bäder</li>
      <li>Reparaturarbeiten</li>
      <li>Silikonarbeiten</li>
      <li>Trockenbau</li>
    </ul>

    <div class="owner-band">
      <div class="owner-name">Jonas Veltmann</div>
      <div class="owner-title">Bachelor Professional im Fliesenlegerhandwerk</div>
    </div>

    <div class="contact-panel">
      <ul class="contact-list">
        <li><span class="contact-icon"><svg viewBox="0 0 16 16"><path d="M3 1l3 3-1.5 2a9 9 0 0 0 5.5 5.5L12 10l3 3-2 2C7 15 1 9 1 3z" fill="#47484b"/></svg></span>05307/4418260</li>
        <li><span class="contact-icon"><svg viewBox="0 0 16 16"><rect x="1.5" y="3.5" width="13" height="9" fill="none" stroke="#47484b" stroke-width="1.5"/><path d="M1.5 3.5l6.5 5 6.5-5" fill="none" stroke="#47484b" stroke-width="1.5"/></svg></span>info@fliesenlegermeister-veltmann.de</li>
        <li><span class="contact-icon"><svg viewBox="0 0 16 16"><path d="M8 15s5-5.5 5-9A5 5 0 0 0 3 6c0 3.5 5 9 5 9z" fill="#47484b"/><circle cx="8" cy="6" r="2" fill="#fff"/></svg></span>Lindenweg 7,<br>38100 Musterstadt</li>
        <li><span class="contact-icon"><svg viewBox="0 0 16 16"><circle cx="8" cy="8" r="6.3" fill="none" stroke="#47484b" stroke-width="1.4"/><ellipse cx="8" cy="8" rx="2.8" ry="6.3" fill="none" stroke="#47484b" stroke-width="1.2"/><path d="M1.7 8h12.6" stroke="#47484b" stroke-width="1.2"/></svg></span>www.fliesenlegermeister-veltmann.de</li>
      </ul>
    </div>

    <svg class="tile-accent" viewBox="0 0 110 274" aria-hidden="true">
      <polygon points="110,0 110,40 26,274 0,274 98,0" fill="#ffffff"/>
      <rect x="48" y="142" width="56" height="56" fill="#0e4e9e" stroke="#ffffff" stroke-width="8" transform="rotate(25 76 170)"/>
    </svg>
  </section>
</body>
</html>
```